300 x 250 Web Ad for Porn Website

300 x 250 web ad that will appear on a porn site. Need to see 3 options, one with each of the 3 girls. Remove the background around the girls.

Underneath the girls image should read in big bold letters: High Speed Internet
Underneath in slightly smaller size: NO Credit Check

To the left of the girl: Save MONEY...

To the right of the girl: So you can buy more PORN

We want it to look very unique, raunchy, and eye catching.

Target Market(s)

Porn website

Industry/Entity Type

Internet Service Provider

Colors

Designer to choose colors to be used in the design.

Requirements
Must have
• Must stand out so people will definitely notice it.
• JPEG and PNG formats

```html
<!DOCTYPE html>
<html lang="en">
<head>
<meta charset="utf-8">
<title>High Speed Internet – Web Ad Options</title>
<link rel="stylesheet" href="https://fonts.googleapis.com/css2?family=Archivo+Black&family=Bowlby+One+SC&display=swap">
<style>
  :root {
    --canvas: #ffffff;
    --magenta: #d8148a;
    --ink: #0d0d0d;
    --ink-soft: #1c1c1c;
    --white: #ffffff;
    --violet: #8b1fb4;
    --tag: #e0188f;
  }
  * { box-sizing: border-box; margin: 0; padding: 0; }
  html, body { width: 1200px; height: 1000px; overflow: hidden; background: var(--canvas); }
  .canvas { position: relative; width: 1200px; height: 1000px; }

  .ad {
    position: absolute;
    width: 507px; height: 422px;
    background: var(--magenta);
    overflow: hidden;
    box-shadow: 3px 4px 6px rgba(0,0,0,0.45);
    font-family: "Archivo Black", "Arial Black", sans-serif;
  }
  .ad--one { left: 90px; top: 67px; }
  .ad--two { left: 630px; top: 69px; }
  .ad--three { left: 347px; top: 529px; }

  .ad__art { position: absolute; inset: 0; width: 507px; height: 422px; }

  .tag {
    position: absolute;
    background: var(--tag);
    color: var(--ink);
    font-size: 22px;
    line-height: 1;
    padding: 7px 10px 6px;
    -webkit-text-stroke: 5px var(--white);
    paint-order: stroke fill;
    z-index: 2;
  }
  .tag--save { left: 30px; top: 58px; transform: rotate(9deg); }
  .tag--money { left: 26px; top: 124px; transform: rotate(5deg); }

  .headline {
    position: absolute;
    right: 22px; top: 24px;
    width: 240px;
    text-align: right;
    z-index: 2;
  }
  .headline__line { display: block; }
  .headline__line > span {
    display: inline-block;
    transform-origin: right center;
  }
  .headline__lead {
    color: var(--white);
    font-size: 20px;
    line-height: 27px;
    -webkit-text-stroke: 6px var(--ink);
    paint-order: stroke fill;
  }
  .headline__punch {
    color: var(--white);
    font-size: 42px;
    line-height: 52px;
    margin-top: 6px;
    -webkit-text-stroke: 8px var(--ink);
    paint-order: stroke fill;
  }
  .headline__offer {
    font-family: "Bowlby One SC", "Arial Black", sans-serif;
    color: var(--ink);
    -webkit-text-stroke: 8px var(--white);
    paint-order: stroke fill;
  }
  .headline__offer--high { font-size: 64px; line-height: 87px; margin-top: 12px; }
  .headline__offer--high > span { transform: scaleX(0.9); }
  .headline__offer--speed { font-size: 64px; line-height: 86px; }
  .headline__offer--speed > span { transform: scaleX(0.74); }
  .headline__offer--internet { font-size: 46px; line-height: 44px; }
  .headline__offer--internet > span { transform: scaleX(0.72); }

  .fineprint {
    position: absolute;
    right: 22px; bottom: 16px;
    color: var(--violet);
    font-size: 25px;
    line-height: 1;
    -webkit-text-stroke: 5px var(--white);
    paint-order: stroke fill;
    z-index: 2;
  }
</style>
</head>
<body>
<main class="canvas">

  <section class="ad ad--one">
    <svg class="ad__art" viewBox="0 0 507 422">
      <defs>
        <pattern id="checker-one" width="8" height="8" patternUnits="userSpaceOnUse">
          <rect width="8" height="8" fill="var(--ink)"/>
          <rect width="4" height="4" fill="var(--ink-soft)"/>
          <rect x="4" y="4" width="4" height="4" fill="var(--ink-soft)"/>
        </pattern>
        <linearGradient id="photo-one" x1="0" y1="0" x2="0" y2="1">
          <stop offset="0" stop-color="#8a5a4c"/>
          <stop offset="0.45" stop-color="#c99a86"/>
          <stop offset="1" stop-color="#d9c2bc"/>
        </linearGradient>
      </defs>
      <polygon class="dark-panel" points="0,0 55,0 175,100 175,422 0,422" fill="url(#checker-one)"/>
      <rect role="img" aria-label="Cut-out photo of a woman in sheer pink lingerie, background removed"
            x="100" y="6" width="232" height="440" rx="18"
            fill="url(#photo-one)" stroke="var(--white)" stroke-width="6"/>
    </svg>
    <span class="tag tag--save">SAVE</span>
    <span class="tag tag--money">MONEY...</span>
    <div class="headline">
      <span class="headline__line headline__lead"><span>SO YOU CAN</span></span>
      <span class="headline__line headline__lead"><span>BUY MORE</span></span>
      <span class="headline__line headline__punch"><span>PORN</span></span>
      <span class="headline__line headline__offer headline__offer--high"><span>High</span></span>
      <span class="headline__line headline__offer headline__offer--speed"><span>Speed</span></span>
      <span class="headline__line headline__offer headline__offer--internet"><span>Internet</span></span>
    </div>
    <span class="fineprint">NO CREDIT CHECK</span>
  </section>

  <section class="ad ad--two">
    <svg class="ad__art" viewBox="0 0 507 422">
      <defs>
        <pattern id="checker-two" width="8" height="8" patternUnits="userSpaceOnUse">
          <rect width="8" height="8" fill="var(--ink)"/>
          <rect width="4" height="4" fill="var(--ink-soft)"/>
          <rect x="4" y="4" width="4" height="4" fill="var(--ink-soft)"/>
        </pattern>
        <linearGradient id="photo-two" x1="0" y1="0" x2="0" y2="1">
          <stop offset="0" stop-color="#3a2624"/>
          <stop offset="0.4" stop-color="#c58f78"/>
          <stop offset="0.7" stop-color="#c0252c"/>
          <stop offset="1" stop-color="#e8d7bd"/>
        </linearGradient>
      </defs>
      <polygon class="dark-panel" points="0,0 55,0 175,100 175,422 0,422" fill="url(#checker-two)"/>
      <rect role="img" aria-label="Cut-out photo of a woman in red lingerie with devil horns and a fur coat, background removed"
            x="34" y="6" width="300" height="440" rx="18"
            fill="url(#photo-two)" stroke="var(--white)" stroke-width="6"/>
    </svg>
    <span class="tag tag--save">SAVE</span>
    <span class="tag tag--money">MONEY...</span>
    <div class="headline">
      <span class="headline__line headline__lead"><span>SO YOU CAN</span></span>
      <span class="headline__line headline__lead"><span>BUY MORE</span></span>
      <span class="headline__line headline__punch"><span>PORN</span></span>
      <span class="headline__line headline__offer headline__offer--high"><span>High</span></span>
      <span class="headline__line headline__offer headline__offer--speed"><span>Speed</span></span>
      <span class="headline__line headline__offer headline__offer--internet"><span>Internet</span></span>
    </div>
    <span class="fineprint">NO CREDIT CHECK</span>
  </section>

  <section class="ad ad--three">
    <svg class="ad__art" viewBox="0 0 507 422">
      <defs>
        <pattern id="checker-three" width="8" height="8" patternUnits="userSpaceOnUse">
          <rect width="8" height="8" fill="var(--ink)"/>
          <rect width="4" height="4" fill="var(--ink-soft)"/>
          <rect x="4" y="4" width="4" height="4" fill="var(--ink-soft)"/>
        </pattern>
        <linearGradient id="photo-three" x1="0" y1="0" x2="0" y2="1">
          <stop offset="0" stop-color="#6b4a3c"/>
          <stop offset="0.4" stop-color="#c58a6a"/>
          <stop offset="1" stop-color="#3a2a26"/>
        </linearGradient>
      </defs>
      <polygon class="dark-panel" points="0,0 55,0 175,100 175,422 0,422" fill="url(#checker-three)"/>
      <rect role="img" aria-label="Cut-out photo of a woman in a black bikini seen from behind, background removed"
            x="56" y="6" width="266" height="440" rx="18"
            fill="url(#photo-three)" stroke="var(--white)" stroke-width="6"/>
    </svg>
    <span class="tag tag--save">SAVE</span>
    <span class="tag tag--money">MONEY...</span>
    <div class="headline">
      <span class="headline__line headline__lead"><span>SO YOU CAN</span></span>
      <span class="headline__line headline__lead"><span>BUY MORE</span></span>
      <span class="headline__line headline__punch"><span>PORN</span></span>
      <span class="headline__line headline__offer headline__offer--high"><span>High</span></span>
      <span class="headline__line headline__offer headline__offer--speed"><span>Speed</span></span>
      <span class="headline__line headline__offer headline__offer--internet"><span>Internet</span></span>
    </div>
    <span class="fineprint">NO CREDIT CHECK</span>
  </section>

</main>
</body>
</html>
```